Health Coaching Brochure for Healthcare Practioners

I am looking to have a tri-fold brochure created marketed towards healthcare practitioners (doctors, nurses, surgeons, etc), to get them to purchase 1-on-1 health coaching from me.
I've provided the text/content (in pdf & pages), my logo, a picture of me, and two color palettes, but please also include lots of white space. I would like to design to be very clean, modern & crisp. Also include additional photos, of doctors, etc taking care of themselves & feeling happy (maybe eating healthy, maybe exercising, feeling good & happy!)
Please also see http://tallbirchwellness.com and http://instagram.com/tallbirchwellness for a feel of my brand.
Thank you!
Target Market(s)
Healthcare Practioners (mainly based in Los Angeles, for now)
Industry/Entity Type
Healthcare
Look and feel
Each slider illustrates characteristics of the customer's brand and the style your logo design should communicate.

```html
<!DOCTYPE html>
<html lang="en">
<head>
<meta charset="utf-8">
<title>Tall Birch Wellness – Tri-fold Brochure</title>
<link href="https://fonts.googleapis.com/css2?family=Montserrat:wght@500;600;700;800&family=Open+Sans:wght@400;600&display=swap" rel="stylesheet">
<style>
  :root{
    --teal:#2aacae;
    --teal-dark:#1f8f91;
    --green:#8cc63f;
    --ink:#4a4f54;
    --muted:#7b8187;
    --paper:#ffffff;
    --stage:#e8e8e8;
  }
  *{box-sizing:border-box;margin:0;padding:0}
  html,body{width:1200px;height:2400px;overflow:hidden}
  body{background:var(--stage);font-family:"Open Sans",Arial,sans-serif;color:var(--ink);position:relative}

  .spread{position:absolute;left:60px;width:1080px;height:834px;display:flex;background:var(--paper);box-shadow:0 2px 6px rgba(0,0,0,.12)}
  .spread--outside{top:200px}
  .spread--inside{top:1300px}
  .panel{position:relative;width:360px;height:100%;overflow:hidden}
  .panel + .panel{border-left:1px solid #eef0f0}

  .photo{position:absolute;left:0;width:100%}
  .wave{position:absolute;left:0;width:100%;display:block}

  .brand{font-family:"Montserrat",Arial,sans-serif;font-weight:600;color:var(--teal);font-size:22px;letter-spacing:.5px;display:flex;align-items:center;gap:8px}
  .brand__dot{width:12px;height:12px;border-radius:50%;background:var(--green)}

  h2,h3{font-family:"Montserrat",Arial,sans-serif}
  .on-teal{color:#fff}
  .panel-title{font-size:20px;font-weight:700;text-transform:uppercase;letter-spacing:1px;margin-bottom:12px}
  .body-text{font-size:13px;line-height:1.6}
  .list{list-style:none;margin-top:14px}
  .list li{font-size:13px;line-height:1.5;padding:5px 0 5px 22px;position:relative}
  .list li::before{content:"";position:absolute;left:0;top:11px;width:9px;height:9px;border-radius:50%;background:var(--green)}

  .ticks{list-style:none}
  .ticks li{display:flex;align-items:center;gap:12px;font-size:14px;padding:10px 0;border-bottom:1px solid #e6eaea}
  .ticks svg{flex:none}

  .pill{display:inline-block;background:var(--green);color:#fff;font-family:"Montserrat",Arial,sans-serif;font-weight:700;font-size:14px;letter-spacing:1.5px;padding:10px 24px;border-radius:3px}

  /* outside – left panel */
  .intro{position:absolute;top:0;left:0;width:100%;height:500px;background:var(--teal);padding:46px 34px}
  .coach-photo{position:absolute;left:34px;top:540px;width:150px;height:150px;border-radius:50%;background:radial-gradient(circle at 45% 40%,#d9b9a3,#6b4a3d 75%)}
  .coach-note{position:absolute;left:200px;top:560px;right:26px}
  .coach-note h3{font-size:15px;color:var(--teal);margin-bottom:6px}
  .coach-note p{font-size:12px;line-height:1.5;color:var(--muted)}
  .band{position:absolute;left:0;bottom:0;width:100%;height:60px;background:var(--teal)}

  /* outside – middle panel */
  .back-content{position:absolute;top:330px;left:34px;right:34px;text-align:center}
  .back-content .brand{justify-content:center;margin-bottom:24px}
  .back-content .body-text{margin-top:22px;color:var(--muted)}
  .smoothie-photo{position:absolute;left:50%;bottom:70px;transform:translateX(-50%);width:170px;height:170px;border-radius:50%;background:radial-gradient(circle at 50% 45%,#b6dc6a,#4f8a2a 75%);border:6px solid #fff;box-shadow:0 0 0 3px var(--green)}

  /* outside – cover */
  .cover-content{position:absolute;top:555px;left:34px;right:30px}
  .cover-title{font-size:26px;font-weight:800;color:var(--teal);line-height:1.1;margin:16px 0 8px;text-transform:uppercase}
  .cover-sub{font-size:13px;color:var(--muted);margin-bottom:12px}
  .contact{font-size:11px;line-height:1.7;color:var(--ink)}

  /* inside – left */
  .benefits{position:absolute;top:400px;left:0;width:100%;bottom:0;background:var(--teal);padding:36px 34px}

  /* inside – middle */
  .steps-head{position:absolute;top:-90px;left:50%;transform:translateX(-50%);width:300px;height:250px;border-radius:50%;background:var(--green);display:flex;align-items:flex-end;justify-content:center;padding-bottom:40px}
  .steps-head h2{color:#fff;font-size:24px;font-weight:800;text-transform:uppercase;letter-spacing:1px}
  .steps{position:absolute;top:210px;left:34px;right:34px}
  .steps .pill{margin-top:36px}
  .steps-cta{text-align:center}

  /* inside – right */
  .testimonial{position:absolute;top:0;left:0;width:100%;height:450px;background:var(--teal);padding:50px 34px}
  .testimonial blockquote{font-size:15px;line-height:1.7;font-style:italic}
  .testimonial cite{display:block;margin-top:14px;font-style:normal;font-weight:600;font-size:13px;color:#dff4f4}
</style>
</head>
<body>

<!-- OUTSIDE -->
<section class="spread spread--outside">
  <!-- inside flap -->
  <div class="panel">
    <div class="intro on-teal">
      <h2 class="panel-title">Why Health Coaching?</h2>
      <p class="body-text">You spend your days caring for others. Coaching gives you the time, tools and support to care for yourself.</p>
      <ul class="list">
        <li>Personalised nutrition plans</li>
        <li>Sustainable exercise routines</li>
        <li>Stress and sleep support</li>
        <li>Accountability every week</li>
      </ul>
    </div>
    <svg class="wave" style="top:470px" viewBox="0 0 360 60" height="60" preserveAspectRatio="none"><path d="M0 30 Q180 70 360 20 L360 0 L0 0Z" fill="var(--teal)"/></svg>
    <div class="coach-photo" role="img" aria-label="Portrait photo of the health coach"></div>
    <div class="coach-note">
      <h3>Meet Your Coach</h3>
      <p>Certified health coach helping busy practitioners thrive.</p>
    </div>
    <div class="band"></div>
  </div>

  <!-- back panel -->
  <div class="panel">
    <div class="photo" style="top:0;height:290px;background:linear-gradient(135deg,#e25a2c,#f2b13b 40%,#7fb23a 75%,#3f7d2a)" role="img" aria-label="Photo of fresh vegetables and healthy food"></div>
    <svg class="wave" style="top:240px" viewBox="0 0 360 70" height="70" preserveAspectRatio="none">
      <path d="M0 40 Q180 0 360 40 L360 70 L0 70Z" fill="#fff"/>
      <path d="M0 40 Q180 0 360 40" fill="none" stroke="var(--green)" stroke-width="4"/>
    </svg>
    <div class="back-content">
      <div class="brand"><span class="brand__dot"></span>Tall Birch Wellness</div>
      <span class="pill">BOOK A FREE CALL</span>
      <p class="body-text">One-on-one coaching designed around long shifts and demanding schedules.</p>
    </div>
    <div class="smoothie-photo" role="img" aria-label="Photo of a green smoothie"></div>
    <div class="band" style="height:40px"></div>
  </div>

  <!-- cover -->
  <div class="panel">
    <div class="photo" style="top:0;height:520px;background:linear-gradient(160deg,#b49a86,#7d6656 55%,#3c3330)" role="img" aria-label="Photo of a woman exercising outdoors in sportswear"></div>
    <svg class="wave" style="top:440px" viewBox="0 0 360 110" height="110" preserveAspectRatio="none">
      <path d="M0 60 Q170 10 360 50 L360 110 L0 110Z" fill="var(--teal)"/>
      <path d="M0 78 Q170 30 360 70 L360 110 L0 110Z" fill="#fff"/>
      <path d="M0 60 Q170 10 360 50" fill="none" stroke="var(--green)" stroke-width="4"/>
    </svg>
    <div class="cover-content">
      <div class="brand"><span class="brand__dot"></span>Tall Birch Wellness</div>
      <h1 class="cover-title">Change<br>the way you live</h1>
      <p class="cover-sub">Health coaching for healthcare practitioners</p>
      <p class="contact">Phone: (555) 010-0199<br>Email: hello@yourwebsite.example<br>Your Street Address Here</p>
    </div>
    <div class="band" style="height:40px"></div>
  </div>
</section>

<!-- INSIDE -->
<section class="spread spread--inside">
  <div class="panel">
    <div class="photo" style="top:0;height:420px;background:linear-gradient(150deg,#f1ece6,#cfc4b8 50%,#8a7768)" role="img" aria-label="Photo of a practitioner doing a plank exercise at home"></div>
    <svg class="wave" style="top:370px" viewBox="0 0 360 60" height="60" preserveAspectRatio="none"><path d="M0 40 Q180 0 360 30 L360 60 L0 60Z" fill="var(--teal)"/><path d="M0 40 Q180 0 360 30" fill="none" stroke="var(--green)" stroke-width="4"/></svg>
    <div class="benefits on-teal">
      <h2 class="panel-title">Your Health Matters</h2>
      <p class="body-text">Long hours and constant pressure take a toll. Small daily changes add up to lasting energy and balance.</p>
      <ul class="list">
        <li>More energy on shift</li>
        <li>Better eating habits</li>
        <li>Less stress, more focus</li>
      </ul>
    </div>
  </div>

  <div class="panel">
    <div class="steps-head"><h2>How It Works</h2></div>
    <div class="steps">
      <ul class="ticks">
        <li><svg width="20" height="20" viewBox="0 0 20 20"><circle cx="10" cy="10" r="10" fill="var(--teal)"/><path d="M5.5 10.5l3 3 6-6.5" fill="none" stroke="#fff" stroke-width="2.2"/></svg>Initial wellness assessment</li>
        <li><svg width="20" height="20" viewBox="0 0 20 20"><circle cx="10" cy="10" r="10" fill="var(--teal)"/><path d="M5.5 10.5l3 3 6-6.5" fill="none" stroke="#fff" stroke-width="2.2"/></svg>Custom nutrition guidance</li>
        <li><svg width="20" height="20" viewBox="0 0 20 20"><circle cx="10" cy="10" r="10" fill="var(--teal)"/><path d="M5.5 10.5l3 3 6-6.5" fill="none" stroke="#fff" stroke-width="2.2"/></svg>Weekly one-on-one sessions</li>
        <li><svg width="20" height="20" viewBox="0 0 20 20"><circle cx="10" cy="10" r="10" fill="var(--teal)"/><path d="M5.5 10.5l3 3 6-6.5" fill="none" stroke="#fff" stroke-width="2.2"/></svg>Movement that fits your day</li>
        <li><svg width="20" height="20" viewBox="0 0 20 20"><circle cx="10" cy="10" r="10" fill="var(--teal)"/><path d="M5.5 10.5l3 3 6-6.5" fill="none" stroke="#fff" stroke-width="2.2"/></svg>Ongoing support by message</li>
      </ul>
      <div class="steps-cta"><span class="pill">START TODAY</span></div>
    </div>
    <div class="band" style="height:40px"></div>
  </div>

  <div class="panel">
    <div class="testimonial on-teal">
      <h2 class="panel-title">What Clients Say</h2>
      <blockquote>Coaching helped me finally take care of myself between shifts. I feel stronger and calmer.<cite>— Registered Nurse</cite></blockquote>
    </div>
    <svg class="wave" style="top:420px" viewBox="0 0 360 60" height="60" preserveAspectRatio="none"><path d="M0 30 Q180 70 360 20 L360 0 L0 0Z" fill="var(--teal)"/><path d="M0 30 Q180 70 360 20" fill="none" stroke="var(--green)" stroke-width="4"/></svg>
    <div class="photo" style="top:500px;bottom:0;background:linear-gradient(135deg,#f6f3ee,#f3b04a 45%,#e2672f 70%,#8fbf45)" role="img" aria-label="Photo of a doctor with fresh fruit and a healthy snack"></div>
  </div>
</section>

</body>
</html>
```